Guaranteed Job - Sleek Sexy Business Card UV Spot

Im looking for a sleek and sexy business card, that resembles elite or VIP status status.
our business is corinvale.example
you can view our products on there, but our main audience for handing out our cards will be for people in the hospitality industry, so it will need to impress high management and CEO of hotels and restaurants, bars, clubs etc...
the card features will have UV spot on both sides, 400gsm stock. standard size.
Artwork should be 86 x 54mm + 2mm bleed = 90 x 58mm
it should have a nice "unique" uv spot pattern that highlights the card, not a repeated pattern, theres no originality there, and it will be disregarded.
The written material will be:
Corin Vale Hospitality College (logo)
Tobin Marsh
Director
Phone: 1300 615 737
Mobile: 0455 817 296
Email: info@corinvale.example
website: www.corinvale.example
I'm looking for originality here, i don't want just a simple stock card, want something that has a wow factor for people.
You will find the logo attached. you may invert the white to black words to suit the background as you please.
thank you and good luck
As a side note, ive received a lot of proposals, im too busy to give feedback to each and every one, so if i havent provided feedback for your design within 24 hours, then consider it not acceptable, and you could resubmit another design.
So far i have not seen any design that stood out for me, they all seem pretty generic. there nothing thats unique, i would figure for the amount that im offering, that people would put some more effort and creativity into the design.
so far over 200 designs submitted, and nothing i have seen looks very original, everything looks like a different variation of the same stuff, i said it very clearly i wanted something unique, the only thing that has come close to it so far is this one
Reason: Ive received alot of design concepts and i have reviewed everyone, but i havent had time to give feedback to every single one, only the ones that have interested me, if i havent responded, its because i havent found it good enough.
so far only a few design have been on par with what ive been looking for, an attractive eye popping design.
heres a few of them,
http://files.pixelbazaar.example/design_img/51736/62418/62418_2840915_51736_image.jpg
http://files.pixelbazaar.example/design_img/51736/68254/68254_2841377_51736_image.jpg
theyre, both unique and original, and eye catching, the only thing theyre missing is the sexyness.
if you still think you have some creativity left in your minds, then throw it on here.
Reason: Sorry guys for the delay, I was in a serious accident and out of commission for the past few months, I'm just slowly recovering now, please bare with me as i try to attend to this project, it may take me awhile as I have other projects that are on standby, I'm not 100% at the moment, so im extending the deadline for 2 weeks right now. Thanks for your patience.
Hospitality

```html
<!DOCTYPE html>
<html lang="en">
<head>
<meta charset="utf-8">
<title>Corin Vale Hospitality College — Business Card</title>
<link rel="stylesheet" href="https://fonts.googleapis.com/css2?family=Titillium+Web:wght@400;600;700&display=swap">
<style>
  :root {
    --page-bg: #d6d6d6;
    --card-dark: #0d1117;
    --card-mid: #15263a;
    --band-top: #4d8db8;
    --band-bottom: #2f6990;
    --accent-blue: #3f9be0;
    --name-blue: #cfe6f7;
    --text-white: #f2f5f8;
    --text-muted: #b9c4ce;
    --icon-stroke: #6fa9d6;
  }
  * { margin: 0; padding: 0; box-sizing: border-box; }
  html, body { width: 1200px; height: 911px; overflow: hidden; }
  body {
    background: var(--page-bg);
    font-family: "Titillium Web", Arial, sans-serif;
    position: relative;
  }
  .card {
    position: absolute;
    top: 275px;
    width: 560px;
    height: 361px;
    overflow: hidden;
    background: var(--card-dark);
  }
  .card--front { left: 30px; }
  .card--back { left: 610px; }
  .card__texture {
    position: absolute; inset: 0;
    background: radial-gradient(ellipse at 45% 40%, var(--card-mid) 0%, #111a25 50%, var(--card-dark) 100%);
  }
  .card__band {
    position: absolute; left: 0; right: 0;
    top: 154px; height: 32px;
    background: linear-gradient(var(--band-top), var(--band-bottom));
    opacity: 0.85;
  }
  .brand {
    position: absolute;
    color: var(--text-white);
    font-weight: 600;
    text-transform: uppercase;
    line-height: 1.05;
    display: flex; align-items: center;
  }
  .brand__mark {
    background: var(--accent-blue);
    border-radius: 50%;
    flex: none;
  }
  .card--front .brand { left: 140px; top: 52px; gap: 14px; font-size: 24px; }
  .card--front .brand__mark { width: 62px; height: 62px; }
  .card--back .brand { left: 100px; top: 88px; gap: 22px; font-size: 38px; }
  .card--back .brand__mark { width: 108px; height: 108px; }
  .brand__name small { display: block; font-size: 0.55em; letter-spacing: 0.06em; }
  .person {
    position: absolute; left: 158px; top: 154px; height: 32px;
    display: flex; align-items: center; gap: 14px;
  }
  .person__name { color: var(--name-blue); font-weight: 700; font-size: 20px; }
  .person__role { color: var(--text-white); font-weight: 600; font-size: 15px; }
  .contact { position: absolute; left: 158px; top: 192px; list-style: none; }
  .contact__row {
    display: flex; align-items: center;
    height: 33.5px;
  }
  .contact__label {
    width: 78px; color: var(--accent-blue); font-weight: 600; font-size: 15px;
  }
  .contact__icon { width: 48px; display: flex; align-items: center; }
  .contact__value { color: var(--text-white); font-weight: 600; font-size: 15px; }
</style>
</head>
<body>
  <section class="card card--front" aria-label="Card front">
    <div class="card__texture" role="img" aria-label="Dark navy damask pattern background"></div>
    <div class="card__band"></div>
    <div class="brand">
      <span class="brand__mark"></span>
      <span class="brand__name">Corin Vale<small>Hospitality College</small></span>
    </div>
    <div class="person">
      <span class="person__name">Tobin Marsh</span>
      <span class="person__role">Director</span>
    </div>
    <ul class="contact">
      <li class="contact__row">
        <span class="contact__label">phone</span>
        <span class="contact__icon">
          <svg width="22" height="22" viewBox="0 0 22 22" fill="none" stroke="var(--icon-stroke)" stroke-width="1.6">
            <circle cx="11" cy="11" r="9.5"/>
            <path d="M7.5 6.5c-1 1 0 4 2 6s5 3 6 2l-1.5-2-1.5 1c-1-.5-2.5-2-3-3l1-1.5z"/>
          </svg>
        </span>
        <span class="contact__value">1300 615 737</span>
      </li>
      <li class="contact__row">
        <span class="contact__label">mobile</span>
        <span class="contact__icon">
          <svg width="22" height="22" viewBox="0 0 22 22" fill="none" stroke="var(--icon-stroke)" stroke-width="1.6">
            <rect x="6" y="2" width="10" height="18" rx="1.5"/>
            <rect x="8" y="4.5" width="6" height="10" fill="var(--icon-stroke)" stroke="none"/>
          </svg>
        </span>
        <span class="contact__value">0455 817 296</span>
      </li>
      <li class="contact__row">
        <span class="contact__label">Email</span>
        <span class="contact__icon">
          <svg width="22" height="22" viewBox="0 0 22 22" fill="none" stroke="var(--icon-stroke)" stroke-width="1.6">
            <rect x="2" y="5" width="18" height="12"/>
            <path d="M2 5l9 7 9-7"/>
          </svg>
        </span>
        <span class="contact__value">info@corinvale.example</span>
      </li>
      <li class="contact__row">
        <span class="contact__label">website</span>
        <span class="contact__icon">
          <svg width="22" height="22" viewBox="0 0 22 22" fill="none" stroke="var(--icon-stroke)" stroke-width="1.4">
            <circle cx="11" cy="11" r="9"/>
            <ellipse cx="11" cy="11" rx="4" ry="9"/>
            <path d="M2 11h18M4 6.5h14M4 15.5h14"/>
          </svg>
        </span>
        <span class="contact__value">www.corinvale.example</span>
      </li>
    </ul>
  </section>

  <section class="card card--back" aria-label="Card back">
    <div class="card__texture" role="img" aria-label="Dark navy damask pattern background"></div>
    <div class="card__band"></div>
    <div class="brand">
      <span class="brand__mark"></span>
      <span class="brand__name">Corin Vale<small>Hospitality College</small></span>
    </div>
  </section>
</body>
</html>
```